New Business Card Design Project

I need a clean, professional business card. I'd like it to have some color, but not be wild. We do technology consulting and we have clients large and small who trust us with some of their most important data and projects. Simple but not boring should drive all design proposals. Multicolored and two sided, but with a matte finish, I think.
For more on tone, check out our website: http://brindlequay.com

Target Market(s)

Upper management of respected businesses. Tech savvy, but not "hipster".

Industry/Entity Type

Business

Requirements
Must have
• Files need to be provided in .eps and in .pdf in a manner that allows for easy updates.
Must have Name, Title, Phone, Email, Twitter, Website
Nice to have
• Logo/Name shouldn't be too big. One thing I've read several places is that the bigger the logo, the smaller the brand. A good article on dos and don'ts here: http://www.mossvane.com/2011/02/business-card-experience.html

```html
<!DOCTYPE html>
<html lang="en">
<head>
<meta charset="utf-8">
<title>Brindlequay Business Card</title>
<link href="https://fonts.googleapis.com/css2?family=Mulish:wght@400;700;800&family=Questrial&display=swap" rel="stylesheet">
<style>
  :root {
    --backdrop: #c9c9c9;
    --paper: #ffffff;
    --teal: #3aa9c4;
    --lime: #95c23d;
    --slate-top: #262626;
    --slate-bottom: #5a5a5a;
    --logo-grey: #8a8a8a;
    --light-text: #e8e8e8;
  }
  html, body { margin: 0; padding: 0; overflow: hidden; }
  .canvas {
    width: 1200px; height: 861px; position: relative; overflow: hidden;
    background: var(--backdrop);
    font-family: "Questrial", "Mulish", sans-serif;
  }
  .card {
    position: absolute; top: 276px; width: 540px; height: 308px;
    background: var(--paper); overflow: hidden;
    box-shadow: 0 6px 18px rgba(0,0,0,.25);
  }
  .card--front { left: 40px; }
  .card--back { left: 620px; }
  .card__rules { position: absolute; left: 0; right: 0; top: 128px; }
  .rule--teal { height: 4px; background: var(--teal); }
  .rule--gap { height: 4px; background: var(--paper); }
  .rule--lime { height: 6px; background: var(--lime); }
  .card__panel {
    position: absolute; left: 0; right: 0; top: 142px; bottom: 0;
    background: linear-gradient(180deg, var(--slate-top) 0%, var(--slate-bottom) 100%);
  }
  .wordmark {
    position: absolute; display: flex; align-items: center; gap: 12px;
    font-family: "Questrial", sans-serif; font-size: 36px; letter-spacing: 2px;
    color: var(--logo-grey); white-space: nowrap;
  }
  .wordmark__mark { width: 22px; height: 22px; background: var(--lime); }
  .card--front .wordmark { left: 30px; top: 66px; font-size: 24px; letter-spacing: 1.5px; gap: 9px; }
  .card--front .wordmark__mark { width: 16px; height: 16px; }
  .card--back .wordmark { left: 50%; transform: translateX(-50%); top: 54px; }
  .person { position: absolute; right: 30px; top: 60px; text-align: right; white-space: nowrap; }
  .person__name {
    font-family: "Mulish", sans-serif; font-weight: 700; font-size: 21px;
    color: var(--teal); letter-spacing: 1px; text-transform: uppercase; line-height: 1.1;
  }
  .person__title { font-size: 14px; color: #3a3a3a; letter-spacing: 1px; }
  .contacts {
    position: absolute; left: 28px; top: 20px; margin: 0; padding: 0; list-style: none;
    color: var(--light-text); font-size: 15px;
  }
  .contacts li { display: flex; align-items: center; gap: 12px; height: 30px; }
  .contacts svg { width: 20px; height: 20px; flex: none; }
  .pitch { position: absolute; left: 0; right: 0; top: 18px; text-align: center; }
  .pitch__lead {
    margin: 0; font-family: "Mulish", sans-serif; font-weight: 800; font-size: 20px;
    color: var(--teal); line-height: 1.2;
  }
  .pitch__turn {
    margin: 0; font-family: "Mulish", sans-serif; font-weight: 800; font-size: 20px;
    color: var(--lime); line-height: 1.2;
  }
  .pitch__body {
    margin: 12px 28px 0; font-family: "Mulish", sans-serif; font-size: 11.5px;
    line-height: 1.45; color: var(--light-text);
  }
</style>
</head>
<body>
<main class="canvas">

  <section class="card card--front" aria-label="Business card front">
    <div class="wordmark"><span class="wordmark__mark"></span><span>BRINDLEQUAY</span></div>
    <div class="person">
      <div class="person__name">Dana Whitlock</div>
      <div class="person__title">CEO</div>
    </div>
    <div class="card__rules">
      <div class="rule--teal"></div><div class="rule--gap"></div><div class="rule--lime"></div>
    </div>
    <div class="card__panel">
      <ul class="contacts">
        <li>
          <svg viewBox="0 0 20 20" aria-hidden="true"><circle cx="10" cy="10" r="9" fill="none" stroke="#95c23d" stroke-width="1.6"/><path d="M7 5.5l2 2-1.2 1.3a6 6 0 0 0 3.4 3.4L12.5 11l2 2-1.4 1.5C9.5 14 6 10.5 5.5 7z" fill="#95c23d"/></svg>
          <span>1-800-555-0142, ext. 700</span>
        </li>
        <li>
          <svg viewBox="0 0 20 20" aria-hidden="true"><circle cx="10" cy="10" r="9" fill="#95c23d"/><rect x="5" y="6.5" width="10" height="7" fill="none" stroke="#2b2b2b" stroke-width="1.3"/><path d="M5 6.5l5 4 5-4" fill="none" stroke="#2b2b2b" stroke-width="1.3"/></svg>
          <span>dana@brindlequay.com</span>
        </li>
        <li>
          <svg viewBox="0 0 20 20" aria-hidden="true"><circle cx="10" cy="10" r="9" fill="#95c23d"/></svg>
          <span>@brindlequay</span>
        </li>
        <li>
          <svg viewBox="0 0 20 20" aria-hidden="true"><circle cx="10" cy="10" r="9" fill="#95c23d"/><circle cx="10" cy="10" r="5" fill="none" stroke="#2b2b2b" stroke-width="1.2"/><path d="M5 10h10M10 5c-2.5 3-2.5 7 0 10M10 5c2.5 3 2.5 7 0 10" fill="none" stroke="#2b2b2b" stroke-width="1"/></svg>
          <span>www.brindlequay.com</span>
        </li>
      </ul>
    </div>
  </section>

  <section class="card card--back" aria-label="Business card back">
    <div class="wordmark"><span class="wordmark__mark"></span><span>BRINDLEQUAY</span></div>
    <div class="card__rules">
      <div class="rule--teal"></div><div class="rule--gap"></div><div class="rule--lime"></div>
    </div>
    <div class="card__panel">
      <div class="pitch">
        <p class="pitch__lead">Your business activity creates data.</p>
        <p class="pitch__turn">We turn data into dollars.</p>
        <p class="pitch__body">Every transaction, customer contact, and pricing decision forms an actionable piece of data. Effectively capturing, learning from, and unleashing the power of this information can be the difference between success and failure.</p>
      </div>
    </div>
  </section>

</main>
</body>
</html>
```